Medical practice in the United States needs a landing page

Our medical practice, based in Dallas, Texas, is called 'Calloway Headache Clinics.' We perform the Calloway Method on patients to treat chronic, severe head pain.

We currently have a landing page for our Chatterbox ads, but we'd like to improve the page's design to increase the lead conversion rate. The landing page contains a form that allows people to register for our free, on-demand informational webinar about the procedure. Either part of the registration form or all of the registration form must be above the fold.

Here is the link to the landing page that needs a more attractive design: https://callowayheadache.example/migraine-treatment-webinars/calloway-treatment-free-patient-webinar/

Once a lead submits the registration form on that page, they are redirected to a different page on the site that contains the webinar video.

Here is a direct link to the page that contains the actual video (note: this is NOT the page for which I am requesting an improved design for this project; I am only including this link so that you can watch the video if you think it will help you create a design for the other page):

https://callowayheadache.example/calloway-headache-clinics-patient-information-webinar/
Updates

Designs look the same

Hello all,

The designs so far have been very impressive! Thank you all for your hard work. Please don't feel compelled to use my exact wording, though, for the description of the webinar. The only requirement is that the form on the page be present and contain the same form fields.

Thanks again!

Target Market(s)

Patients with chronic, severe head pain

Industry/Entity Type

Healthcare

Requirements
Must have
• Either part of the registration form or all of the registration form must be above the fold.
Should not have
• The registration form located completely below the fold.

```html
<!DOCTYPE html>
<html lang="en">
<head>
<meta charset="utf-8">
<title>Calloway Headache Clinics – Webinar Registration</title>
<link href="https://fonts.googleapis.com/css2?family=Poppins:wght@400;500;600&display=swap" rel="stylesheet">
<style>
  :root {
    --navy: #034a63;
    --green: #7dc242;
    --button-green: #5f9c13;
    --hero-bg: #edf2f9;
    --form-bg: #d3e9ef;
    --white: #ffffff;
    --field-border: #c9e0e4;
    --label: #2d2d2d;
    --placeholder: #777777;
  }
  * { box-sizing: border-box; margin: 0; padding: 0; }
  html, body { width: 1200px; height: 1025px; overflow: hidden; }
  body {
    position: relative;
    background: var(--white);
    font-family: 'Poppins', sans-serif;
    color: var(--navy);
  }

  /* Header */
  .site-header {
    position: absolute; left: 0; top: 0; width: 1200px; height: 92px;
    background: var(--navy);
  }
  .brand-panel {
    position: absolute; left: 0; top: 2px; width: 296px; height: 86px;
  }
  .brand-panel svg { position: absolute; left: 0; top: 0; }
  .brand-name {
    position: absolute; left: 18px; top: 30px;
    font-size: 20px; font-weight: 500; color: var(--navy); letter-spacing: -0.3px;
    white-space: nowrap;
  }
  .main-nav {
    position: absolute; left: 440px; top: 28px;
    display: flex; gap: 0;
  }
  .nav-item {
    display: flex; flex-direction: column; align-items: center;
    color: var(--green); font-size: 11.5px; text-decoration: none;
    margin-right: 44px;
  }
  .nav-item svg { width: 26px; height: 24px; margin-bottom: 3px; fill: var(--green); }
  .nav-item .caret { font-size: 8px; margin-left: 2px; }

  /* Hero */
  .hero {
    position: absolute; left: 0; top: 98px; width: 1200px; height: 271px;
    background: var(--hero-bg); text-align: center;
  }
  .hero h1 {
    margin-top: 70px; font-size: 56px; font-weight: 400; line-height: 1.1; letter-spacing: 0.5px;
  }
  .hero p { margin-top: 10px; font-size: 22.5px; font-weight: 400; }

  /* Registration */
  .registration {
    position: absolute; left: 0; top: 375px; width: 1200px; height: 462px;
    background: var(--form-bg);
  }
  .registration h2 {
    position: absolute; left: 0; top: 16px; width: 1200px; text-align: center;
    font-size: 32px; font-weight: 500;
  }
  .consult-photo {
    position: absolute; left: 47px; top: 117px; width: 346px; height: 230px;
    border-radius: 10px;
    background: linear-gradient(120deg, #d8c7b4 0%, #efe9e2 40%, #b9a391 65%, #2a2420 100%);
  }
  .form-card {
    position: absolute; left: 500px; top: 91px; width: 601px; height: 333px;
    background: var(--white); border-radius: 3px;
  }
  .form-row { position: absolute; left: 14px; }
  .form-row label { position: absolute; left: 0; font-size: 15.5px; color: var(--label); white-space: nowrap; }
  .field {
    position: absolute; left: 150px; width: 338px; height: 34px;
    border: 1px solid var(--field-border); border-radius: 4px;
    font-size: 15.5px; color: var(--placeholder); padding: 5px 5px;
  }
  .row-first { top: 30px; } .row-first label { top: 15px; }
  .row-last { top: 87px; } .row-last label { top: 15px; }
  .row-subject { top: 144px; } .row-subject label { top: 14px; }
  .row-subject .field { height: 110px; }
  .submit-btn {
    position: absolute; left: 34px; top: 279px; width: 156px; height: 32px;
    background: var(--button-green); color: var(--white); border-radius: 3px;
    font-size: 16.5px; font-weight: 500; text-align: center; line-height: 32px;
  }

  /* Footer */
  .site-footer {
    position: absolute; left: 0; top: 842px; width: 1200px; height: 183px;
    background: var(--navy); color: var(--white);
  }
  .footer-brand {
    position: absolute; left: 150px; top: 60px; font-size: 22px; font-weight: 400; white-space: nowrap;
  }
  .footer-col { position: absolute; top: 28px; font-size: 13.5px; line-height: 20.5px; }
  .footer-col h3 { font-size: 13.5px; font-weight: 600; }
  .contact-col { left: 525px; }
  .contact-line { display: flex; align-items: center; gap: 8px; }
  .contact-line svg { width: 18px; height: 16px; fill: var(--white); }
  .menu-col { left: 792px; }
  .social-links { position: absolute; left: 1006px; top: 58px; display: flex; gap: 12px; }
  .social-dot { width: 18px; height: 18px; border-radius: 50%; background: var(--white); }
  .copyright {
    position: absolute; left: 0; top: 145px; width: 1200px; text-align: center; font-size: 13.5px;
  }
</style>
</head>
<body>

<header class="site-header">
  <div class="brand-panel">
    <svg width="296" height="86" viewBox="0 0 296 86">
      <path d="M0 0 H284 C280 40 268 70 246 86 H0 Z" fill="#ffffff"/>
      <path d="M284 0 C280 40 268 70 246 86" fill="none" stroke="#7dc242" stroke-width="3"/>
    </svg>
    <span class="brand-name">calloway headache clinics</span>
  </div>
  <nav class="main-nav">
    <a class="nav-item">
      <svg viewBox="0 0 26 24"><path d="M13 2 L25 12 H21 V22 H15 V15 H11 V22 H5 V12 H1 Z"/></svg>Home
    </a>
    <a class="nav-item">
      <svg viewBox="0 0 26 24"><circle cx="13" cy="6" r="5"/><path d="M3 23 C3 15 7 12 13 12 C19 12 23 15 23 23 Z"/></svg>Our Team Doctors
    </a>
    <a class="nav-item">
      <svg viewBox="0 0 26 24"><path d="M5 2 V9 C5 14 13 14 13 9 V2" fill="none" stroke="#7dc242" stroke-width="2.5"/><path d="M9 13 V17 C9 22 19 22 19 16 V12" fill="none" stroke="#7dc242" stroke-width="2.5"/><circle cx="19" cy="10" r="3"/></svg>Services
    </a>
    <a class="nav-item">
      <svg viewBox="0 0 26 24"><path d="M1 3 H25 V21 H1 Z M4 7 V17 H12 V7 Z M15 8 V10 H22 V8 Z M15 12 V14 H22 V12 Z"/></svg>Contact
    </a>
    <a class="nav-item">
      <svg viewBox="0 0 26 24"><circle cx="13" cy="7" r="6"/><path d="M2 23 C2 16 7 14 13 14 C19 14 24 16 24 23 Z"/></svg><span>Profile <span class="caret">▼</span></span>
    </a>
  </nav>
</header>

<section class="hero">
  <h1>Calloway Headache Clinics</h1>
  <p>We perform the Calloway Method on patients to treat chronic, severe head pain</p>
</section>

<section class="registration">
  <h2>Registration form</h2>
  <div class="consult-photo" role="img" aria-label="Photo of a doctor in a white coat talking with a patient across a desk"></div>
  <form class="form-card">
    <div class="form-row row-first"><label>First Name</label><div class="field">Your name..</div></div>
    <div class="form-row row-last"><label>Last Name</label><div class="field">Your last name..</div></div>
    <div class="form-row row-subject"><label>Subject</label><div class="field">Write something..</div></div>
    <div class="submit-btn">Submit</div>
  </form>
</section>

<footer class="site-footer">
  <div class="footer-brand">calloway headache clinics</div>
  <div class="footer-col contact-col">
    <h3>Address</h3>
    <div class="contact-line">
      <svg viewBox="0 0 18 16"><path d="M3 1 L6 1 L8 5 L6 7 C7 9 9 11 11 12 L13 10 L17 12 L17 15 C10 16 2 8 3 1 Z"/></svg>000-000-0000
    </div>
    <div class="contact-line">
      <svg viewBox="0 0 18 16"><path d="M1 3 H17 V13 H1 Z" /><path d="M1 3 L9 9 L17 3" fill="none" stroke="#034a63" stroke-width="1.5"/></svg>hello@callowayclinics.example
    </div>
    <div>detail address, DTAIL ADDRESS</div>
  </div>
  <div class="footer-col menu-col">
    <h3>Menu</h3>
    <div>Home</div>
    <div>Our team doctors Us</div>
    <div>Services</div>
    <div>Contact Us</div>
  </div>
  <div class="social-links">
    <span class="social-dot" aria-label="Social link"></span>
    <span class="social-dot" aria-label="Chatterbox"></span>
    <span class="social-dot" aria-label="Social link"></span>
  </div>
  <div class="copyright">calloway headache clinics | 2023 | All Rights Reserved</div>
</footer>

</body>
</html>
```